Real Estate Brokerage - Sales Promo Flyer

We would like someone to design a 8x11 high gloss promotional flyer for our real estate agents to use in the field when presenting to a possible listing client (someone who wants to sell their home).

The flyer should include some of our brokerage's recent sales transaction numbers, as well as benefits to using our service.

We would like our design to have a professional appeal, with bold colors, and vivid images.

I have attached 5 images of recently sold homes:
247 Marisol Lane Trust, Palm Beach Gardens, Florida - Sold for $424,000
4718 Tierra Linda Ct, Boca Raton, FL 33431 - Sold for $415,000
418 Verbena Hills Drive, Palm Beach Gardens, Florida - Sold for $877,500
20417 Heron Bluff Circle, West Palm Beach, Florida - Sold for $380,000
382 Thistle Road, Greenacres, Florida - Sold for $234,500

I can provide any additional details you need. See attached files.
Updates

This flyer should contain our business name, logo, phone numbers, and website (however you see fit). PelicoHomes Palm Beach County | (561) 402-1186 Broward County | (954) 238-4417 www.pelicohomes-example.com

More Properties to Add: 418 Verbena Hills Drive, Palm Beach Gardens, Florida - Sold for $877,500 20417 Heron Bluff Circle, West Palm Beach, Florida - Sold for $380,000 382 Thistle Road, Greenacres, Florida - Sold for $234,500

I have added the Original Logo Images. Please use one of these in your design.

I have uploaded an image of our syndication partners, please add this to your flyers.

Please submit all of your Design. Thanks!

Please submit your edits

Industry/Entity Type

Real Estate

Requirements
Must have
• PelicoHomes is one word with a capital K and capital R.

Must have website and phone number.

PelicoHomes
www.pelicohomes-example.com
561-402-1186 - Palm Beach County
954-238-4417 - Broward County

```html
<!DOCTYPE html>
<html lang="en">
<head>
<meta charset="utf-8">
<title>PelicoHomes – Sales Flyer</title>
<link href="https://fonts.googleapis.com/css2?family=Open+Sans:wght@400;600;700&family=Oswald:wght@500;600&family=PT+Sans+Narrow:wght@700&family=Tinos:ital,wght@1,700&display=swap" rel="stylesheet">
<style>
  :root{
    --backdrop-dark:#1c1c1c;
    --backdrop-mid:#5a5a5a;
    --paper:#f4f6f6;
    --blue-deep:#0a63b4;
    --blue:#1187d6;
    --blue-light:#19b3ea;
    --cyan-text:#1bb0e0;
    --ink:#1a1a1a;
    --gray-text:#555d63;
    --fact-box:#5e5e5e;
    --white:#ffffff;
  }
  *{box-sizing:border-box;margin:0;padding:0}
  html,body{width:999px;height:1200px;overflow:hidden}
  body{
    background:radial-gradient(ellipse at center,var(--backdrop-mid) 0%,#3a3a3a 55%,var(--backdrop-dark) 100%);
    font-family:"Open Sans",sans-serif;color:var(--ink);position:relative;
  }
  .flyer{position:absolute;left:90px;top:87px;width:820px;height:1061px;background:var(--paper);overflow:hidden}
  .flyer > *{position:absolute}
  .brand{left:26px;top:40px;display:flex;align-items:center;gap:14px}
  .brand-dot{width:44px;height:44px;border-radius:50%;background:var(--blue-light)}
  .brand-name{font-family:"Open Sans",sans-serif;font-weight:600;font-size:28px;letter-spacing:4px;color:#4a4a4a}
  .shapes{left:0;top:0}
  .headline{left:0;top:128px;width:820px;text-align:center;color:var(--white);font-weight:700;font-size:21px;line-height:29px}
  .sold{top:234px;width:189px;height:228px;border-radius:6px;background:linear-gradient(180deg,var(--blue) 0%,var(--blue-light) 100%);color:var(--white);font-family:"Tinos",serif;font-style:italic;font-weight:700;text-align:center}
  .sold-price{font-size:22px;margin-top:8px}
  .sold-photo{margin:10px auto 0;width:181px;height:122px;border:3px solid var(--white);border-radius:8px}
  .sold-address{font-size:15px;line-height:22px;margin-top:8px;white-space:nowrap}
  .band-name{left:32px;top:500px;font-family:"Oswald",sans-serif;font-weight:600;font-size:49px;line-height:60px;color:var(--white);white-space:nowrap}
  .band-tag{left:410px;top:518px;font-family:"PT Sans Narrow",sans-serif;font-weight:700;font-size:29px;color:var(--gray-text);white-space:nowrap}
  .caps-title{font-family:"PT Sans Narrow",sans-serif;font-weight:700;color:var(--cyan-text);font-variant:small-caps;letter-spacing:.5px;white-space:nowrap}
  .facts-title{left:430px;top:614px;font-size:26px}
  .facts-box{left:537px;top:612px;width:247px;height:107px;background:var(--fact-box);border-radius:8px;color:var(--white);font-size:16.5px;line-height:22.5px;padding:4px 0 0 12px;list-style:none;white-space:nowrap}
  .facts-box li::before,.listing li::before{content:"●";display:inline-block;width:36px;font-size:12px;vertical-align:1px}
  .listing-title{left:32px;top:650px;font-size:23px}
  .listing{left:32px;top:690px;width:470px;list-style:none;font-size:13.6px;line-height:19.5px}
  .listing li{padding-left:24px;text-indent:-24px}
  .listing li::before{width:24px;text-indent:0;color:#666}
  .body-copy{left:28px;top:788px;width:770px;font-size:14.3px;line-height:19.5px}
  .body-copy p{margin-bottom:19px}
  .office{top:979px;font-weight:700;white-space:nowrap}
  .office-label{font-size:17px}
  .office-phone{font-size:23px;margin-top:2px}
  .web{left:470px;top:1016px;font-size:18px;letter-spacing:1.6px;color:var(--white);white-space:nowrap}
</style>
</head>
<body>
<div class="flyer">
  <svg class="shapes" width="820" height="1061" viewBox="0 0 820 1061" aria-hidden="true">
    <defs>
      <linearGradient id="bandBlue" x1="0" x2="1" y1="0" y2="0">
        <stop offset="0" stop-color="#19b3ea"/><stop offset="1" stop-color="#0a6fc2"/>
      </linearGradient>
      <linearGradient id="deepBlue" x1="0" x2="1"><stop offset="0" stop-color="#0a63b4"/><stop offset="1" stop-color="#1190dd"/></linearGradient>
    </defs>
    <polygon points="466,73 820,73 820,196 440,196" fill="url(#deepBlue)"/>
    <rect x="0" y="120" width="820" height="76" fill="url(#bandBlue)"/>
    <rect x="0" y="488" width="820" height="18" fill="#19b3ea"/>
    <polygon points="0,497 410,497 362,561 0,561" fill="url(#deepBlue)"/>
    <polygon points="452,988 820,988 820,1043 420,1043" fill="url(#deepBlue)"/>
    <rect x="0" y="1043" width="820" height="18" fill="#19b3ea"/>
  </svg>

  <div class="brand"><span class="brand-dot"></span><span class="brand-name">PelicoHomes</span></div>

  <p class="headline">INVENTORY IS AT AN ALL TIME LOW AND PRICES ARE GOING WAY UP!<br>QUALIFIED BUYERS ARE WAITING FOR GREAT HOMES LIKE YOURS.</p>

  <div class="sold" style="left:20px">
    <p class="sold-price">Sold for $424,000</p>
    <div class="sold-photo" role="img" aria-label="Photo of sold home, palm trees and lawn" style="background:linear-gradient(180deg,#9cc3e6 0%,#d9c6a8 55%,#5e9b3e 100%)"></div>
    <p class="sold-address">247 Marisol Lane Trust<br>Palm Beach Gardens Florida</p>
  </div>
  <div class="sold" style="left:218px">
    <p class="sold-price">Sold for $380,000</p>
    <div class="sold-photo" role="img" aria-label="Photo of sold ranch home with driveway" style="background:linear-gradient(180deg,#e6eef2 0%,#6f7a63 50%,#4f8f34 100%)"></div>
    <p class="sold-address">20417 Heron Bluff Circle<br>West Palm Beach, Florida</p>
  </div>
  <div class="sold" style="left:416px">
    <p class="sold-price">Sold for $415,000</p>
    <div class="sold-photo" role="img" aria-label="Photo of sold home behind a large tree" style="background:linear-gradient(180deg,#9fc6e4 0%,#4e8a36 50%,#c9b39c 100%)"></div>
    <p class="sold-address">4718 Tierra Linda Ct<br>Boca Raton, FL 33431</p>
  </div>
  <div class="sold" style="left:615px">
    <p class="sold-price">Sold for $234,500</p>
    <div class="sold-photo" role="img" aria-label="Photo of sold home with garage and shrubs" style="background:linear-gradient(180deg,#b8d3ea 0%,#a9adab 50%,#4d7d3a 100%)"></div>
    <p class="sold-address">382 Thistle Road<br>Greenacres, Florida</p>
  </div>

  <p class="band-name">PELICOHOMES</p>
  <p class="band-tag">is Selling Homes for Top Dollar.</p>

  <p class="caps-title facts-title">The Facts:</p>
  <ul class="facts-box">
    <li>64 sales year to date</li>
    <li>15 sales over 200k</li>
    <li>8 sales over 300k</li>
    <li>Sale of the Year $877.5k</li>
  </ul>

  <p class="caps-title listing-title">Where We List You Home</p>
  <ul class="listing">
    <li>Multiple Listing Service (MLS)</li>
    <li>30+ Real Estate Websites (Homevista, Nestorly, HouseLift, Yondr, Orbix Real Estate, Keypads)</li>
    <li style="white-space:nowrap">30+ Social Media Websites (Friendwall, Chirpline, Searchly+, Pinboardly)</li>
  </ul>

  <div class="body-copy">
    <p>By listing your home with PelicoHomes, you will receive maximum exposure, more offers, and ultimately will sell your home faster than listing with a traditional real estate brokerage.</p>
    <p>Our proven marketing system drives a greater volume of traffic to your listing than any of our competitors.</p>
    <p>PelicoHomes is recognized as a real estate leader in both Palm Beach and Broward County. Our knowledgable agents and aggressive marketing will make sure that you get the best price for your home, in the least amount of time.</p>
  </div>

  <div class="office" style="left:26px"><p class="office-label">Palm Beach County</p><p class="office-phone">(561) 402-1186</p></div>
  <div class="office" style="left:232px"><p class="office-label">Broward County</p><p class="office-phone">(954) 238-4417</p></div>
  <p class="web">www.pelicohomes-example.com</p>
</div>
</body>
</html>
```